Accounting and Financial Services Firm - Modern, Fresh, Original, Professional

We need a business card designed. We would like to see use of the the colors blue. Logo attached.

Modern, Fresh, Original, Professional,
Updates

Email section on business card required. design brief updated.

Target Market(s)

Small to medium businesses and high net worth individuals

Industry/Entity Type

Public Accounting

Contact Information for Business Card

Business Name: PM Ledgerline Chartered Accountants
Address: Level 14, 82 Harrow Lane Sydney NSW 2000
Ph: 02 9314 2587
Mobile: 04 XXXX XXXX
Email: anna@pmledgerline.com.au
ChatLine ID: XXXXXXX
Website: www.pmledgerline.com.au

Name: Anna Petrov
Position: Manager

Font styles to use
Sans Serif

Colors
0492cd
33a6d7
85cae6

Requirements
Must have
• Modern font.

```html
<!DOCTYPE html>
<html lang="en">
<head>
<meta charset="utf-8">
<title>PM Ledgerline Chartered Accountants – Business Card</title>
<link rel="stylesheet" href="https://fonts.googleapis.com/css2?family=Nunito+Sans:wght@300;400;700&display=swap">
<style>
  :root {
    --brand-blue: #0492cd;
    --mid-blue: #33a6d7;
    --light-blue: #85cae6;
    --card-white: #ffffff;
    --text-grey: #5f6368;
    --rule-grey: #d5dbe0;
    --stage: #eceff2;
  }
  * { margin: 0; padding: 0; box-sizing: border-box; }
  html, body {
    width: 1200px; height: 862px; overflow: hidden;
    background: var(--stage);
    font-family: "Nunito Sans", Arial, sans-serif;
  }
  .canvas { position: relative; width: 1200px; height: 862px; }

  .card {
    position: absolute; width: 560px; height: 320px;
    box-shadow: 0 6px 18px rgba(0,0,0,0.12);
    overflow: hidden;
  }

  /* Front */
  .card-front {
    left: 80px; top: 90px;
    background: var(--brand-blue);
    color: var(--card-white);
    display: flex; flex-direction: column; align-items: center; justify-content: center;
  }
  .front-name {
    font-weight: 400; font-size: 34px; letter-spacing: 3px;
    text-align: center; line-height: 1.15; text-transform: uppercase;
    margin-top: 10px;
  }
  .front-name small { display: block; font-size: 13px; letter-spacing: 4px; }
  .front-web {
    position: absolute; bottom: 46px; left: 0; right: 0;
    text-align: center; font-size: 14px; letter-spacing: 0.5px;
  }

  /* Back */
  .card-back {
    left: 560px; top: 450px;
    background: var(--card-white);
  }
  .back-name {
    position: absolute; left: 40px; top: 120px; width: 300px;
    color: var(--brand-blue);
    font-weight: 400; font-size: 30px; letter-spacing: 2.5px;
    text-transform: uppercase; line-height: 1.15;
  }
  .back-name small { display: block; font-size: 11.5px; letter-spacing: 3.6px; }
  .divider {
    position: absolute; left: 346px; top: 40px; width: 1px; height: 186px;
    background: var(--rule-grey);
  }
  .contact {
    position: absolute; left: 364px; top: 38px; width: 190px;
    color: var(--text-grey); font-size: 12px; line-height: 1.6;
  }
  .contact-name { color: var(--brand-blue); font-weight: 700; font-size: 18px; line-height: 1.2; }
  .contact-role { margin-bottom: 6px; }
  .contact-line { display: flex; align-items: center; gap: 7px; white-space: nowrap; }
  .contact-line svg { width: 11px; height: 11px; fill: var(--brand-blue); flex: none; }
  .band {
    position: absolute; left: 0; right: 0; bottom: 0; height: 46px;
    background: var(--brand-blue); color: var(--card-white);
    font-size: 13px; display: flex; align-items: center; justify-content: flex-end;
    padding-right: 40px;
  }
</style>
</head>
<body>
<main class="canvas">
  <section class="card card-front" aria-label="Card front">
    <div class="front-name">PM Ledgerline<small>Chartered Accountants</small></div>
    <div class="front-web">www.pmledgerline.com.au</div>
  </section>

  <section class="card card-back" aria-label="Card back">
    <div class="back-name">PM Ledgerline<small>Chartered Accountants</small></div>
    <div class="divider"></div>
    <div class="contact">
      <div class="contact-name">Anna Petrov</div>
      <div class="contact-role">Manager</div>
      <div>Level 14, 82 Harrow Lane Sydney</div>
      <div>NSW 2000</div>
      <div class="contact-line">
        <svg viewBox="0 0 24 24" aria-hidden="true"><path d="M6.6 10.8a15.1 15.1 0 0 0 6.6 6.6l2.2-2.2a1 1 0 0 1 1-.25 11.4 11.4 0 0 0 3.6.57 1 1 0 0 1 1 1V20a1 1 0 0 1-1 1A17 17 0 0 1 3 4a1 1 0 0 1 1-1h3.5a1 1 0 0 1 1 1c0 1.25.2 2.45.57 3.57a1 1 0 0 1-.25 1z"/></svg>
        02 9314 2587
      </div>
      <div class="contact-line">
        <svg viewBox="0 0 24 24" aria-hidden="true"><path d="M7 1h10a2 2 0 0 1 2 2v18a2 2 0 0 1-2 2H7a2 2 0 0 1-2-2V3a2 2 0 0 1 2-2zm0 3v14h10V4zm5 15.5a1.2 1.2 0 1 0 0 2.4 1.2 1.2 0 0 0 0-2.4z"/></svg>
        04 XXXX XXXX
      </div>
      <div class="contact-line">
        <svg viewBox="0 0 24 24" aria-hidden="true"><path d="M3 5h18a1 1 0 0 1 1 1v12a1 1 0 0 1-1 1H3a1 1 0 0 1-1-1V6a1 1 0 0 1 1-1zm1 2.4V17h16V7.4l-8 5.3zM5.5 7 12 11.3 18.5 7z"/></svg>
        anna@pmledgerline.com.au
      </div>
      <div class="contact-line">
        <svg viewBox="0 0 24 24" aria-hidden="true"><path d="M12 2a10 10 0 1 0 0 20 10 10 0 0 0 0-20zm6.9 6h-2.9a15.7 15.7 0 0 0-1.4-3.6A8 8 0 0 1 18.9 8zM12 4c.8 1.2 1.5 2.5 1.9 4h-3.8c.4-1.5 1.1-2.8 1.9-4zM4.3 14a8 8 0 0 1 0-4h3.4a16.5 16.5 0 0 0 0 4zm.8 2h2.9c.3 1.3.8 2.5 1.4 3.6A8 8 0 0 1 5.1 16zM8 8H5.1a8 8 0 0 1 4.3-3.6C8.8 5.5 8.3 6.7 8 8zm4 12c-.8-1.2-1.5-2.5-1.9-4h3.8c-.4 1.5-1.1 2.8-1.9 4zm2.3-6H9.7a14.7 14.7 0 0 1 0-4h4.6a14.7 14.7 0 0 1 0 4zm.3 5.6c.6-1.1 1.1-2.3 1.4-3.6h2.9a8 8 0 0 1-4.3 3.6zM16.3 14a16.5 16.5 0 0 0 0-4h3.4a8 8 0 0 1 0 4z"/></svg>
        www.pmledgerline.com.au
      </div>
    </div>
    <div class="band">ChatLine ID: XXXXXXX</div>
  </section>
</main>
</body>
</html>
```